indépendant en tant que Massothérapeute et Préparateur Mental, j'ai besoin de ...

Massothérapeute et préparateur mental indépendant, je recherche une carte de visite sobre et dynamique, sans images liées au massage ou à la préparation mentale mais intégrant mon logo. Les couleurs que j'aime bien sont : Blanc, gris, anthracite, noir et jaune

Contact Information for Business Card

carte de préférence Horizontale
neutre qui puisse toucher le deux domaines Massothérapie et préparation mentale

Requirements
Must have
• mon projet doit intégrer au recto:
LOGO
Loïc Vermande
078 315 26 49
info@loicvermande-exemple.ch
et éventuellement www.loicvermande-exemple.ch

et au verso les deux adresses:

Chemin des Ormelets 27B
1400 Yverdon-les-Bains

Rue des Tanneries 9
1700 Fribourg

Should not have
• mon projet ne doit pas contenir d'image en liens avec le massage ni la préparation mentale.

```html
<!DOCTYPE html>
<html lang="fr">
<head>
<meta charset="utf-8">
<title>Loïc Vermande – Carte de visite</title>
<link rel="stylesheet" href="https://fonts.googleapis.com/css2?family=Montserrat:wght@600;700&family=Roboto:wght@400&display=swap">
<style>
  :root {
    --backdrop: #9b9b9b;
    --card-white: #ffffff;
    --card-dark: #2a2627;
    --ink: #1f1d1e;
    --ink-soft: #444244;
    --metal: #b9b3b5;
    --metal-dim: #6a6466;
  }
  * { margin: 0; padding: 0; box-sizing: border-box; }
  html, body { width: 1200px; height: 1200px; overflow: hidden; }
  body { background: var(--backdrop); position: relative; font-family: "Roboto", Arial, sans-serif; }

  .card {
    position: absolute;
    left: 262px;
    width: 686px;
    height: 380px;
    border-radius: 26px;
    overflow: hidden;
  }
  .card--front { top: 165px; background: var(--card-white); }
  .card--back { top: 653px; background: var(--card-dark); }

  .brand {
    position: absolute;
    text-align: right;
  }
  .card--front .brand { right: 39px; top: 54px; }
  .brand__name {
    font-family: "Montserrat", Arial, sans-serif;
    font-weight: 700;
    font-size: 25px;
    letter-spacing: 1px;
    color: var(--ink);
    line-height: 1;
  }
  .brand__role {
    font-family: "Montserrat", Arial, sans-serif;
    font-weight: 600;
    font-size: 14px;
    font-variant: small-caps;
    letter-spacing: 0.8px;
    color: var(--ink);
    margin-top: 8px;
    line-height: 1;
  }

  .contact {
    position: absolute;
    left: 43px;
    bottom: 36px;
    list-style: none;
    font-size: 15.5px;
    color: var(--ink-soft);
  }
  .contact li { display: flex; align-items: center; height: 19.5px; }
  .contact svg { width: 12px; height: 12px; margin-right: 9px; fill: var(--ink); flex: none; }

  .addresses {
    position: absolute;
    right: 39px;
    bottom: 35px;
    text-align: right;
    font-size: 15.5px;
    color: var(--ink-soft);
    font-style: normal;
    line-height: 19px;
  }
  .addresses p + p { margin-top: 7px; }

  .card--back .brand {
    left: 0; right: 0;
    top: 170px;
    text-align: center;
  }
  .card--back .brand__name { color: var(--metal); font-size: 30px; }
  .card--back .brand__role { color: var(--metal-dim); font-size: 15px; margin-top: 10px; }
</style>
</head>
<body>

<section class="card card--front" aria-label="Recto">
  <div class="brand">
    <p class="brand__name">Loïc VERMANDE</p>
    <p class="brand__role">Massothérapeute / Préparateur Mental</p>
  </div>

  <ul class="contact">
    <li>
      <svg viewBox="0 0 24 24" aria-hidden="true"><path d="M6.6 10.8a15.1 15.1 0 0 0 6.6 6.6l2.2-2.2c.3-.3.7-.4 1-.2 1.1.4 2.3.6 3.6.6.6 0 1 .4 1 1V20c0 .6-.4 1-1 1A17 17 0 0 1 3 4c0-.6.4-1 1-1h3.5c.6 0 1 .4 1 1 0 1.3.2 2.5.6 3.6.1.3 0 .7-.2 1z"/></svg>
      078 315 26 49
    </li>
    <li>
      <svg viewBox="0 0 24 24" aria-hidden="true"><path d="M2 5h20v14H2z M4 7v.4l8 5.2 8-5.2V7z" fill-rule="evenodd"/></svg>
      info@loicvermande-exemple.ch
    </li>
    <li>
      <svg viewBox="0 0 24 24" aria-hidden="true"><circle cx="12" cy="12" r="10"/><path d="M12 2c3 3 3 17 0 20M12 2c-3 3-3 17 0 20M2 12h20" stroke="#fff" stroke-width="1.6" fill="none"/></svg>
      www.loicvermande-exemple.ch
    </li>
  </ul>

  <address class="addresses">
    <p>Rue des Tanneries 9<br>1700 Fribourg</p>
    <p>Chemin des Ormelets 27B<br>1400 Yverdon-les-Bain</p>
  </address>
</section>

<section class="card card--back" aria-label="Verso">
  <div class="brand">
    <p class="brand__name">Loïc VERMANDE</p>
    <p class="brand__role">Massothérapeute / Préparateur Mental</p>
  </div>
</section>

</body>
</html>
```